E Liquid Label design R

Im starting by seying that i dont speak or write Inglés, i dont speak spanish since i am from Paraguay, im very sorry for That, try my best to get Understood. I am startin a company of e liquids, (electronic cigarrettes). the liquid production is ok but the label is not. i try to do my label here with a graphic designer (friend of mine) but is is very busy esta days and I HAD no time for esta. but have made me one label, that i will atach here, That is nice, but is not that i want, because i tell him the name will be "corvex" (the first alchemist in the world) i tell him that i wanted to explore themes like magic, vapors, etc. mistery but looking now is kind of boring. I really like something more hip and modern with a design work, What i do know is that i want to put a red wax seal on the top center of the glass bottle (will attach pics) i really really like the tinbrook artwork, simple, hip, modern, fix in your mind. will attach pics for Those Who dont know the brand, also like the i want to design for 30 ml bottles made of clear glass with dropper (childproof) approx 40 x 90 milimeters in size. i am starting with 8 flavors, so, the design has to be adaptable for each flavor. It has to say somewere the strength level of nicotine 0 -3-6 - 9 to 12 mg in a creative way, maybe some stairs With the levels and the level it has to say Highlighted somewere USA made with ingredients, with some flag or something in the small font section will be warnings, ingredients and other stuff that i will update tomorrow.

Target Market(s)

quitting smokers, vapers

Requirements
Must have
• network (or maybe other color) wax seal as described in the description i wiil update in soon esta sección
Nice to have

```html
<!DOCTYPE html>
<html lang="en">
<head>
<meta charset="utf-8">
<title>Corvex E-Liquid Labels</title>
<link rel="stylesheet" href="https://fonts.googleapis.com/css2?family=Roboto+Condensed:wght@400;700&display=swap">
<style>
  :root {
    --backdrop: #a7a7a7;
    --paper: #ffffff;
    --ink: #111111;
    --strawberry: #d9261c;
    --mint: #17ada0;
    --level-0: #d3d3d3;
    --level-3: #9dc75f;
    --level-6: #1e8a3f;
    --level-9: #ec7f1c;
    --level-12: #e0261e;
    --emblem-dark: #2a2a2a;
    --emblem-light: #e9e9e9;
    --flag-blue: #2c3f8f;
    --flag-red: #c8252c;
  }
  * { box-sizing: border-box; margin: 0; padding: 0; }
  html, body { width: 1105px; height: 1200px; overflow: hidden; }
  body {
    background: var(--backdrop);
    font-family: "Roboto Condensed", "Arial Narrow", sans-serif;
    color: var(--ink);
    position: relative;
  }
  .label {
    position: absolute;
    left: 101px;
    width: 901px;
    height: 449px;
    background: var(--paper);
    border-radius: 27px;
    overflow: hidden;
    box-shadow: 6px 8px 14px rgba(0,0,0,0.35);
  }
  .label--strawberry { top: 117px; --flavor: var(--strawberry); }
  .label--mint { top: 636px; --flavor: var(--mint); }

  .warnings {
    position: absolute;
    left: 13px; top: 19px;
    width: 262px;
    font-size: 12.1px;
    line-height: 12.05px;
  }
  .warnings strong { font-weight: 700; }
  .volume {
    position: absolute;
    left: 65px; top: 370px;
    font-size: 30px;
    line-height: 1;
  }

  .brand {
    position: absolute;
    left: 249px; width: 400px; top: 18px;
    text-align: center;
    font-size: 62px;
    font-weight: 400;
    line-height: 1;
    letter-spacing: 1px;
  }
  .product-type {
    position: absolute;
    left: 249px; width: 400px; top: 83px;
    text-align: center;
    font-size: 24px;
    font-weight: 700;
    color: var(--flavor);
    line-height: 1;
  }
  .emblem {
    position: absolute;
    left: 334px; top: 120px;
    width: 230px; height: 230px;
    border-radius: 50%;
    background: radial-gradient(circle, var(--emblem-light) 0%, var(--paper) 45%, var(--emblem-light) 70%, var(--emblem-dark) 71%, var(--emblem-dark) 72%, var(--paper) 73%);
  }

  .strength {
    position: absolute;
    left: 327px; top: 355px;
    width: 248px;
  }
  .strength__levels {
    display: flex;
    font-size: 17px;
    line-height: 1;
  }
  .strength__levels span { flex: 1; text-align: center; }
  .strength__bar {
    display: flex;
    height: 20px;
    margin-top: 6px;
    border-radius: 10px;
    overflow: hidden;
  }
  .strength__bar span { flex: 1; position: relative; }
  .strength__bar .l0 { background: var(--level-0); }
  .strength__bar .l3 { background: var(--level-3); }
  .strength__bar .l6 { background: var(--level-6); }
  .strength__bar .l9 { background: var(--level-9); }
  .strength__bar .l12 { background: var(--level-12); }
  .strength__bar svg { position: absolute; left: 13px; top: 1px; }

  .info {
    position: absolute;
    left: 672px; top: 23px;
    width: 215px;
    font-size: 17px;
    line-height: 19px;
  }
  .info p + p { margin-top: 19px; }
  .info strong { font-weight: 700; }

  .origin {
    position: absolute;
    left: 672px; top: 264px;
    width: 215px;
    display: flex;
    align-items: center;
    gap: 8px;
  }
  .origin__flag {
    width: 44px; height: 55px;
    flex: none;
    border-radius: 50% 50% 50% 50% / 60% 60% 40% 40%;
    background: linear-gradient(180deg, var(--flag-blue) 0%, var(--flag-blue) 35%, var(--flag-red) 35%, var(--paper) 55%, var(--flag-red) 75%, var(--paper) 100%);
  }
  .origin__text {
    font-size: 16px;
    line-height: 18px;
    text-align: center;
    flex: 1;
  }

  .flavor-band {
    position: absolute;
    left: 0; right: 0; bottom: 0;
    height: 44px;
    background: var(--flavor);
    color: var(--paper);
    text-align: center;
    font-size: 19px;
    font-weight: 700;
    line-height: 44px;
    padding-right: 2px;
  }
  .flavor-band span { position: absolute; left: 0; width: 898px; }
</style>
</head>
<body>

<section class="label label--strawberry">
  <div class="warnings">
    <p><strong>WARNING:</strong> Our products may contain nicotine, wich is highly addictive. Not for sale to minors. Product not recommended for pregnant women and people with cardiovascular problems. Lock up an keep out of the reach of children and pets. In case of CONTACT TO SKIN: Wash thoroughly with soap and water. If you feel unwell consult a doctor ASAP, and keep product container or label with you.</p>
    <p><strong>ATENCION:</strong> Nuestros productos podrian o no contener nicotina, la cual es altamente adictiva. NO debe venderse a menores. Producto no recomendado para mujeres embarazadas y personas con problemas cardiovasculares. Mantener bajo llave y lejos del alcance de niños y mascotas. En caso de CONTACO CON LA PIEL: lavar con abundante agua y jabon. Si usando este producto se siente mareado y/o con otras molestias, consulte con un Doctor inmediatamente, llevando consigo el envase o la etiqueta de este producto.</p>
  </div>
  <div class="volume">30ml</div>

  <h1 class="brand">Corvex</h1>
  <div class="product-type">E-LIQUID</div>
  <div class="emblem" role="img" aria-label="Geometric alchemy emblem: triangle and star inside a ringed circle"></div>

  <div class="strength">
    <div class="strength__levels"><span>0mg</span><span>3mg</span><span>6mg</span><span>9mg</span><span>12mg</span></div>
    <div class="strength__bar">
      <span class="l0"></span><span class="l3"></span><span class="l6"></span><span class="l9"></span>
      <span class="l12"><svg width="24" height="18" viewBox="0 0 24 18"><path d="M2 9 L9 15 L22 2" fill="none" stroke="#fff" stroke-width="2.4"/></svg></span>
    </div>
  </div>

  <div class="info">
    <p><strong>INGREDIENTS:</strong> USP Vegetable Glycerin, USP Propylene Glycol, Natural and Artificial food Flavorings.</p>
    <p><strong>Manufactured by:</strong> Corvex Ltd, Arden Vale, Kestrel Business Park USA<br>info@corvex.com<br>www.corvex.com</p>
  </div>
  <div class="origin">
    <div class="origin__flag" role="img" aria-label="Droplet with the US flag"></div>
    <div class="origin__text">Made with ingredients from the USA</div>
  </div>

  <div class="flavor-band"><span>STRAWBERRY</span></div>
</section>

<section class="label label--mint">
  <div class="warnings">
    <p><strong>WARNING:</strong> Our products may contain nicotine, wich is highly addictive. Not for sale to minors. Product not recommended for pregnant women and people with cardiovascular problems. Lock up an keep out of the reach of children and pets. In case of CONTACT TO SKIN: Wash thoroughly with soap and water. If you feel unwell consult a doctor ASAP, and keep product container or label with you.</p>
    <p><strong>ATENCION:</strong> Nuestros productos podrian o no contener nicotina, la cual es altamente adictiva. NO debe venderse a menores. Producto no recomendado para mujeres embarazadas y personas con problemas cardiovasculares. Mantener bajo llave y lejos del alcance de niños y mascotas. En caso de CONTACO CON LA PIEL: lavar con abundante agua y jabon. Si usando este producto se siente mareado y/o con otras molestias, consulte con un Doctor inmediatamente, llevando consigo el envase o la etiqueta de este producto.</p>
  </div>
  <div class="volume">30ml</div>

  <h1 class="brand">Corvex</h1>
  <div class="product-type">E-LIQUID</div>
  <div class="emblem" role="img" aria-label="Geometric alchemy emblem: triangle and star inside a ringed circle"></div>

  <div class="strength">
    <div class="strength__levels"><span>0mg</span><span>3mg</span><span>6mg</span><span>9mg</span><span>12mg</span></div>
    <div class="strength__bar">
      <span class="l0"></span><span class="l3"></span><span class="l6"></span><span class="l9"></span>
      <span class="l12"><svg width="24" height="18" viewBox="0 0 24 18"><path d="M2 9 L9 15 L22 2" fill="none" stroke="#fff" stroke-width="2.4"/></svg></span>
    </div>
  </div>

  <div class="info">
    <p><strong>INGREDIENTS:</strong> USP Vegetable Glycerin, USP Propylene Glycol, Natural and Artificial food Flavorings.</p>
    <p><strong>Manufactured by:</strong> Corvex Ltd, Arden Vale, Kestrel Business Park USA<br>info@corvex.com<br>www.corvex.com</p>
  </div>
  <div class="origin">
    <div class="origin__flag" role="img" aria-label="Droplet with the US flag"></div>
    <div class="origin__text">Made with ingredients from the USA</div>
  </div>

  <div class="flavor-band"><span>MINT</span></div>
</section>

</body>
</html>
```